Daily Deals Website Needs a Landing Page (Home Page will act as the landing page)

We need a landing page for a daily deals website that will act as the home page. We have attached the wire frame and logo for reference. Open to creative ideas and suggestions as long as the main elements of the wireframe are incorporated in the design. Need a very simplistic design approach like Vorplex's search page. (www.vorplex.com) . Very clean and distinct CTA's.

Target Market(s)

Customers looking for deals on everyday use items

Font styles to use
Sans Serif

Requirements
Must have
• clean design, lots of white space and strong CTA .
Nice to have
• need a clean design overall. Strong CTA
Should not have
• Cluttered look. Too many colors, keep it simple

```html
<!DOCTYPE html>
<html lang="en">
<head>
<meta charset="utf-8">
<title>Dealvio – Best Deals Everyday</title>
<link rel="stylesheet" href="https://fonts.googleapis.com/css2?family=Open+Sans:ital,wght@0,400;0,600;0,700;0,800;1,800&display=swap">
<style>
  :root {
    --bg: #d3dbf7;
    --bg-footer: #e4e9fb;
    --navy: #28398c;
    --navy-dark: #1c2a6b;
    --green: #3b9a3f;
    --leaf: #a6d38f;
    --banner-green: #58b94a;
    --orange: #f7a21b;
    --orange-dark: #e8901a;
    --ink: #1d1d2b;
    --white: #ffffff;
  }
  * { box-sizing: border-box; margin: 0; padding: 0; }
  html, body { width: 798px; height: 1200px; overflow: hidden; }
  body {
    position: relative;
    background: var(--bg);
    font-family: "Open Sans", Arial, sans-serif;
    color: var(--ink);
  }
  .decor { position: absolute; inset: 0; width: 798px; height: 1200px; }
  .brand {
    position: absolute; left: 0; right: 0; text-align: center;
    font-weight: 800; color: var(--navy); letter-spacing: 2px;
  }
  .brand--header { top: 118px; font-size: 86px; line-height: 1; }
  .tagline {
    position: absolute; top: 218px; left: 0; right: 0; text-align: center;
    font-size: 36px; font-weight: 600; color: var(--green);
  }
  .lead {
    position: absolute; left: 0; right: 0; text-align: center; color: var(--ink);
  }
  .lead--small { top: 314px; font-size: 17px; }
  .lead--large { top: 695px; font-size: 28px; line-height: 1.3; }
  .cta {
    position: absolute; left: 266px; width: 266px; height: 64px;
    display: flex; align-items: center; justify-content: center;
    background: var(--orange); color: var(--white);
    font-size: 28px; font-weight: 600; text-decoration: none;
    border-bottom: 3px solid var(--orange-dark);
  }
  .cta--top { top: 340px; }
  .cta--bottom { top: 780px; }
  .deal-card {
    position: absolute; top: 479px; width: 346px; height: 182px;
    overflow: hidden; display: flex;
  }
  .deal-card--featured { left: 47px; background: var(--navy-dark); }
  .deal-card--promoted { left: 407px; background: var(--banner-green); }
  .deal-card__text { width: 170px; padding: 56px 0 0 16px; color: var(--white); }
  .deal-card__title {
    font-size: 27px; font-weight: 800; font-style: italic; line-height: 1;
    text-transform: uppercase;
  }
  .deal-card__sub { font-size: 13px; margin: 4px 0 10px 4px; }
  .deal-card__btn {
    display: inline-block; background: var(--orange); color: var(--white);
    font-size: 10px; font-weight: 700; padding: 5px 12px; margin-left: 4px;
  }
  .deal-card__photo { flex: 1; }
  .deal-card--featured .deal-card__photo {
    background: linear-gradient(120deg, #3a4776, #9aa2b8 55%, #2b3150);
  }
  .deal-card--promoted .deal-card__photo {
    background: linear-gradient(120deg, #d9a7a6, #6ec45c 45%, #2f6fc9);
  }
  .site-footer {
    position: absolute; left: 0; top: 1052px; width: 798px; height: 148px;
    background: var(--bg-footer);
  }
  .brand--footer { top: 34px; font-size: 52px; line-height: 1; }
  .copyright {
    position: absolute; top: 109px; left: 0; right: 0; text-align: center;
    font-size: 12px; color: var(--ink);
  }
</style>
</head>
<body>
  <svg class="decor" viewBox="0 0 798 1200" aria-hidden="true">
    <polygon points="0,0 112,0 0,92" fill="var(--leaf)"/>
    <polygon points="660,0 798,0 798,128 740,108" fill="var(--leaf)"/>
    <polygon points="0,800 120,900 0,1000" fill="var(--leaf)" opacity="0.85"/>
    <polygon points="798,760 798,985 690,985" fill="var(--leaf)" opacity="0.85"/>
  </svg>

  <header>
    <div class="brand brand--header">DEALVIO</div>
    <p class="tagline">Best Deals Everyday</p>
  </header>

  <main>
    <p class="lead lead--small">Get all the best deals directly to your email</p>
    <a class="cta cta--top" href="#">Sign Up Now!</a>

    <section class="deal-card deal-card--featured">
      <div class="deal-card__text">
        <div class="deal-card__title">Featured</div>
        <div class="deal-card__sub">Deal of the Day</div>
        <span class="deal-card__btn">Get It Now!</span>
      </div>
      <div class="deal-card__photo" role="img" aria-label="Row of smartphones in dark and silver finishes"></div>
    </section>

    <section class="deal-card deal-card--promoted">
      <div class="deal-card__text">
        <div class="deal-card__title">Promoted</div>
        <div class="deal-card__sub">Deal of the Day</div>
        <span class="deal-card__btn">Get It Now!</span>
      </div>
      <div class="deal-card__photo" role="img" aria-label="Smartwatch beside a blue smartphone"></div>
    </section>

    <p class="lead lead--large">Get all the best deals<br>directly to your email</p>
    <a class="cta cta--bottom" href="#">Sign Up Now!</a>
  </main>

  <footer class="site-footer">
    <div class="brand brand--footer">DEALVIO</div>
    <p class="copyright">Copyright © 2021 Dealvio. All rights reserved.</p>
  </footer>
</body>
</html>
```